Disability Service Provider needs a flyer

Project Description:
We are seeking a creative and engaging flyer design to promote a twelve week independent living skills program, focusing on key areas such as money management, basic cooking, food safety, and personal well-being and interpersonal skills. The flyer will be used to encourage individuals to enhance their abilities to live independently and confidently.

Target Audience:
Our target audience includes young adults with a disability and individuals transitioning into independent living situations. We aim to reach those who may be new to managing their own finances, cooking for themselves, and maintaining a healthy lifestyle.

Key Messages:

Independent Living Skills: Emphasize the importance of acquiring essential skills for independent living.
Money Management: Highlight budgeting tips, saving strategies, and financial planning.
Basic Cooking: Showcase simple recipes, cooking techniques, and meal preparation tips.
Food Safety: Provide information on safe food handling practices, storage guidelines, and hygiene.
Personal Well-being: Promote self-care practices, stress management techniques, and mental health awareness.

Target Market(s)

Young adults looking to live independently on their own or with friends

Industry/Entity Type

community services sector

Colors
0054AA
0677BA
7BADD7
CADEEF
E8F1F8

Requirements
Must have
• refer to brief

```html
<!DOCTYPE html>
<html lang="en">
<head>
<meta charset="utf-8">
<title>Elevate Your Independence – Twelve-Week Program</title>
<link href="https://fonts.googleapis.com/css2?family=Krona+One&family=Lexend:wght@400;500;600&display=swap" rel="stylesheet">
<style>
  :root {
    --blue-deep: #0054AA;
    --blue-mid: #0677BA;
    --blue-soft: #7BADD7;
    --blue-pale: #CADEEF;
    --blue-mist: #E8F1F8;
    --ink: #2b2b2b;
    --navy: #0d2f45;
    --white: #ffffff;
  }
  * { margin: 0; padding: 0; box-sizing: border-box; }
  html, body { width: 849px; height: 1200px; overflow: hidden; background: var(--white); }
  .flyer {
    position: relative; width: 849px; height: 1200px; overflow: hidden;
    background: var(--white); font-family: 'Lexend', sans-serif; color: var(--ink);
  }
  .backdrop, .scene { position: absolute; left: 0; top: 0; }
  .brand {
    position: absolute; top: 50px; left: 0; width: 849px;
    display: flex; justify-content: center; align-items: center; gap: 10px;
  }
  .brand-dot { width: 34px; height: 34px; border-radius: 50%; background: var(--blue-mid); }
  .brand-name { font-weight: 600; font-size: 31px; color: var(--navy); letter-spacing: -0.5px; }
  .title-frame {
    position: absolute; left: 139px; top: 120px; width: 567px; height: 101px;
    border: 2px solid var(--ink); border-bottom: none;
  }
  .title-frame::before, .title-frame::after {
    content: ""; position: absolute; bottom: 0; height: 2px; background: var(--ink); width: 26px;
  }
  .title-frame::before { left: -2px; }
  .title-frame::after { right: -2px; width: 29px; }
  .headline { position: absolute; left: 172px; top: 144px; font-family: 'Krona One', sans-serif; font-weight: 400; line-height: 1; }
  .headline-top { display: block; font-size: 42px; color: var(--ink); letter-spacing: 1px; }
  .headline-main { display: block; margin-top: 4px; font-size: 47px; color: var(--blue-soft); letter-spacing: 0.3px; }
  .program { position: absolute; top: 258px; left: 0; width: 849px; text-align: center; }
  .program-call { font-weight: 600; font-size: 20px; color: var(--ink); letter-spacing: 0.2px; }
  .program-call em { font-style: normal; color: var(--blue-deep); }
  .program-sub { font-size: 19px; font-weight: 400; color: var(--ink); }
  .skills { position: absolute; left: 85px; top: 325px; width: 690px; }
  .skill { height: 61px; }
  .skill:first-child { height: 57px; }
  .skill h2 {
    font-family: 'Krona One', sans-serif; font-weight: 400; font-size: 11px;
    color: var(--blue-deep); letter-spacing: 0.6px; margin-bottom: 3px;
  }
  .skill p { font-size: 10.4px; line-height: 13.5px; color: var(--ink); }
  .contact { position: absolute; left: 0; top: 1120px; width: 849px; height: 80px; color: var(--white); }
  .phone { position: absolute; left: 66px; top: 28px; font-family: 'Krona One', sans-serif; font-size: 25px; letter-spacing: 0.3px; }
  .address { position: absolute; right: 53px; top: 24px; font-weight: 600; font-size: 14px; }
  .web { position: absolute; right: 53px; top: 53px; font-weight: 600; font-size: 11px; }
</style>
</head>
<body>
<main class="flyer">
  <svg class="backdrop" width="849" height="1200" viewBox="0 0 849 1200" aria-hidden="true">
    <path d="M494 0 C530 150 620 300 849 348 L849 0 Z" fill="var(--blue-mist)"/>
    <path d="M0 333 C180 320 360 360 430 430 C520 520 560 590 600 640 L0 700 Z" fill="var(--blue-mist)"/>
  </svg>

  <svg class="scene" width="849" height="1200" viewBox="0 0 849 1200">
    <defs>
      <linearGradient id="courtTones" x1="0" y1="0" x2="0" y2="1">
        <stop offset="0" stop-color="#8c8778"/>
        <stop offset="0.35" stop-color="#a8927a"/>
        <stop offset="0.6" stop-color="#6e8c8c"/>
        <stop offset="1" stop-color="#35625f"/>
      </linearGradient>
      <radialGradient id="courtLight" cx="0.55" cy="0.45" r="0.6">
        <stop offset="0" stop-color="#e9d3b4" stop-opacity="0.55"/>
        <stop offset="1" stop-color="#e9d3b4" stop-opacity="0"/>
      </radialGradient>
      <linearGradient id="gardenTones" x1="0" y1="0" x2="0" y2="1">
        <stop offset="0" stop-color="#7d8a5c"/>
        <stop offset="0.4" stop-color="#b89a7e"/>
        <stop offset="0.7" stop-color="#5a5a55"/>
        <stop offset="1" stop-color="#8d8882"/>
      </linearGradient>
      <radialGradient id="gardenLight" cx="0.45" cy="0.4" r="0.55">
        <stop offset="0" stop-color="#f0d8c4" stop-opacity="0.5"/>
        <stop offset="1" stop-color="#f0d8c4" stop-opacity="0"/>
      </radialGradient>
    </defs>
    <path d="M0 727 C220 640 400 612 560 620 C700 628 800 660 849 690 L849 1200 L0 1200 Z" fill="var(--blue-pale)"/>
    <path d="M0 820 C120 700 300 628 470 622 C640 616 780 680 849 742 L849 1200 L0 1200 Z" fill="var(--blue-deep)"/>
    <g role="img" aria-label="Photo: two young men in wheelchairs smiling on an outdoor basketball court, one holding a basketball">
      <path d="M0 830 C160 760 330 725 586 724 L500 1200 L0 1200 Z" fill="url(#courtTones)"/>
      <path d="M0 830 C160 760 330 725 586 724 L500 1200 L0 1200 Z" fill="url(#courtLight)"/>
    </g>
    <g role="img" aria-label="Photo: young woman in a wheelchair giving a peace sign outdoors">
      <path d="M601 745 C700 760 790 800 849 845 L849 1200 L510 1200 Z" fill="url(#gardenTones)"/>
      <path d="M601 745 C700 760 790 800 849 845 L849 1200 L510 1200 Z" fill="url(#gardenLight)"/>
    </g>
    <path d="M586 724 L601 745 L510 1200 L500 1200 Z" fill="var(--white)"/>
    <path d="M0 1128 C150 1116 300 1128 450 1122 C600 1116 740 1124 849 1120 L849 1200 L0 1200 Z" fill="var(--blue-deep)"/>
    <path d="M380 1160 C520 1140 700 1150 849 1138 L849 1200 L330 1200 Z" fill="var(--blue-mid)" opacity="0.5"/>
  </svg>

  <header class="brand">
    <span class="brand-dot"></span>
    <span class="brand-name">Brightpath Care</span>
  </header>

  <div class="title-frame"></div>
  <h1 class="headline">
    <span class="headline-top">ELEVATE YOUR</span>
    <span class="headline-main">INDEPENDENCE</span>
  </h1>

  <section class="program">
    <p class="program-call">JOIN OUR <em>TWELVE-WEEK PROGRAM!</em></p>
    <p class="program-sub">Unlock essential life skills like</p>
  </section>

  <section class="skills">
    <article class="skill">
      <h2>INDEPENDENT LIVING SKILLS:</h2>
      <p>Acquiring essential skills for independent living is paramount for a self-sufficient and empowered lifestyle. Discover the importance of mastering key life skills to thrive independently.</p>
    </article>
    <article class="skill">
      <h2>MONEY MANAGEMENT:</h2>
      <p>Explore valuable budgeting tips, savvy saving strategies, and effective financial planning to secure a stable and prosperous future. Empower yourself with the knowledge to achieve financial well-being.</p>
    </article>
    <article class="skill">
      <h2>BASIC COOKING:</h2>
      <p>Immerse yourself in a world of flavor with our showcase of simple recipes, essential cooking techniques, and insightful meal preparation tips. Elevate your culinary skills and savor the joy of creating delicious meals effortlessly.</p>
    </article>
    <article class="skill">
      <h2>FOOD SAFETY:</h2>
      <p>Learn the essentials of safe food handling practices, effective storage guidelines, and impeccable hygiene. Dive into the core of maintaining food safety to ensure health and vitality. Your journey to a healthier lifestyle begins with these vital insights.</p>
    </article>
    <article class="skill">
      <h2>PERSONAL WELL-BEING:</h2>
      <p>Embark on a journey of self-discovery with our promotion of self-care practices, stress management techniques, and heightened mental health awareness. Prioritize your well-being and discover the keys to a balanced and resilient life.</p>
    </article>
  </section>

  <footer class="contact">
    <p class="phone">1300 555 019</p>
    <p class="address">7/40 Harbour Lane Riverton QLD 4100, Australia</p>
    <p class="web">www.brightpathcare.com.au</p>
  </footer>
</main>
</body>
</html>
```